indépendant en tant que Massothérapeute et Préparateur Mental, j'ai besoin de ...

Massothérapeute et préparateur mental indépendant, je recherche une carte de visite sobre et dynamique, sans images liées au massage ou à la préparation mentale mais intégrant mon logo. Les couleurs que j'aime bien sont : Blanc, gris, anthracite, noir et jaune

Contact Information for Business Card

carte de préférence Horizontale
neutre qui puisse toucher le deux domaines Massothérapie et préparation mentale

Requirements
Must have
• mon projet doit intégrer au recto:
LOGO
Loïc Vermande
078 315 26 49
info@loicvermande-exemple.ch
et éventuellement www.loicvermande-exemple.ch

et au verso les deux adresses:

Chemin des Ormelets 27B
1400 Yverdon-les-Bains

Rue des Tanneries 9
1700 Fribourg

Should not have
• mon projet ne doit pas contenir d'image en liens avec le massage ni la préparation mentale.

```html
<!DOCTYPE html>
<html lang="fr">
<head>
<meta charset="utf-8">
<title>Loïc Vermande – Cartes de visite</title>
<link rel="stylesheet" href="https://fonts.googleapis.com/css2?family=Questrial&display=swap">
<style>
  :root {
    --stage: #e4e2de;
    --white: #f4f4f4;
    --grey: #dcdcdc;
    --black: #0b0b0b;
    --anthracite: #1c1c1c;
    --yellow: #d9b51a;
    --yellow-bright: #f0d000;
    --text-dark: #111111;
    --text-light: #f2f2f2;
  }
  * { margin: 0; padding: 0; box-sizing: border-box; }
  html, body { width: 1200px; height: 780px; overflow: hidden; }
  body {
    background: var(--stage);
    font-family: "Questrial", "Helvetica Neue", Arial, sans-serif;
    position: relative;
  }
  .card {
    position: absolute;
    top: 225px;
    width: 560px;
    height: 320px;
    overflow: hidden;
    box-shadow: 0 6px 18px rgba(0,0,0,0.18);
  }
  .card--front { left: 27px; background: var(--black); }
  .card--back { left: 613px; background: var(--black); }

  /* Front */
  .front-head {
    position: absolute; left: 0; top: 0; width: 100%; height: 140px;
    background: linear-gradient(180deg, var(--white), var(--grey));
  }
  .identity {
    position: absolute; display: flex; align-items: center; gap: 18px;
  }
  .front-head .identity { left: 44px; top: 34px; }
  .identity__square {
    width: 58px; height: 58px; background: var(--black);
  }
  .identity__name {
    font-size: 36px; color: var(--text-dark); line-height: 1; letter-spacing: 0.5px;
  }
  .identity__role {
    font-size: 10.5px; color: var(--text-dark); letter-spacing: 1.6px;
    text-transform: uppercase; margin-top: 7px;
  }
  .front-body {
    position: absolute; left: 0; top: 140px; width: 100%; height: 132px;
    background: var(--black); color: var(--text-light);
    display: flex; justify-content: space-between; padding: 20px 34px 0 44px;
  }
  .contact__name {
    color: var(--yellow); font-size: 22px; margin-bottom: 9px;
  }
  .contact__line, .address {
    display: flex; align-items: center; gap: 8px; font-size: 13px; margin-bottom: 5px;
  }
  .icon { width: 16px; height: 16px; flex: none; }
  .addresses { padding-top: 8px; }
  .address { align-items: flex-start; margin-bottom: 12px; line-height: 1.3; }
  .address .icon { margin-top: 2px; }
  .front-band {
    position: absolute; left: 0; bottom: 0; width: 100%; height: 48px;
    background: linear-gradient(180deg, var(--yellow-bright), var(--yellow));
    border-top: 2px solid #3a3a3a;
    display: flex; align-items: center; justify-content: center;
    color: var(--text-dark); font-size: 15px; letter-spacing: 0.3px;
  }

  /* Back */
  .back-band {
    position: absolute; left: 0; top: 94px; width: 100%; height: 132px;
    background: linear-gradient(180deg, var(--white), var(--grey));
    border-top: 4px solid var(--yellow-bright);
    border-bottom: 4px solid var(--yellow-bright);
    box-shadow: 0 0 0 3px var(--white) inset;
  }
  .back-band .identity { left: 50%; top: 50%; transform: translate(-50%, -50%); }
</style>
</head>
<body>

<section class="card card--front" aria-label="Recto">
  <header class="front-head">
    <div class="identity">
      <div class="identity__square"></div>
      <div>
        <div class="identity__name">Loïc Vermande</div>
        <div class="identity__role">Massothérapeute / Préparateur mental</div>
      </div>
    </div>
  </header>

  <div class="front-body">
    <div class="contact">
      <div class="contact__name">Loïc Vermande</div>
      <div class="contact__line">
        <svg class="icon" viewBox="0 0 16 16"><circle cx="8" cy="8" r="8" fill="#d9b51a"/><path d="M5.2 4.2l1.4-.3 1 2-1 .8c.4.9 1 1.6 1.9 2l.8-1 2 1-.3 1.4c-2.9.2-6-2.8-5.8-5.9z" fill="#0b0b0b"/></svg>
        078 315 26 49
      </div>
      <div class="contact__line">
        <svg class="icon" viewBox="0 0 16 16"><circle cx="8" cy="8" r="8" fill="#d9b51a"/><rect x="4" y="5.2" width="8" height="5.6" fill="#0b0b0b"/><path d="M4 5.2l4 3 4-3" stroke="#d9b51a" stroke-width="0.9" fill="none"/></svg>
        info@loicvermande-exemple.ch
      </div>
      <div class="contact__line">
        <svg class="icon" viewBox="0 0 16 16"><circle cx="8" cy="8" r="8" fill="#d9b51a"/><circle cx="8" cy="8" r="4.3" fill="none" stroke="#0b0b0b" stroke-width="0.9"/><path d="M3.7 8h8.6M8 3.7c-2 2.4-2 6.2 0 8.6M8 3.7c2 2.4 2 6.2 0 8.6" stroke="#0b0b0b" stroke-width="0.8" fill="none"/></svg>
        www.loicvermande-exemple.ch
      </div>
    </div>

    <div class="addresses">
      <div class="address">
        <svg class="icon" viewBox="0 0 16 16"><circle cx="8" cy="8" r="8" fill="#d9b51a"/><path d="M8 3.6a2.9 2.9 0 0 0-2.9 2.9C5.1 8.6 8 12.2 8 12.2s2.9-3.6 2.9-5.7A2.9 2.9 0 0 0 8 3.6z" fill="#0b0b0b"/><circle cx="8" cy="6.5" r="1.1" fill="#d9b51a"/></svg>
        <span>Chemin des Ormelets 27B<br>1400 Yverdon-les-Bains</span>
      </div>
      <div class="address">
        <svg class="icon" viewBox="0 0 16 16"><circle cx="8" cy="8" r="8" fill="#d9b51a"/><path d="M8 3.6a2.9 2.9 0 0 0-2.9 2.9C5.1 8.6 8 12.2 8 12.2s2.9-3.6 2.9-5.7A2.9 2.9 0 0 0 8 3.6z" fill="#0b0b0b"/><circle cx="8" cy="6.5" r="1.1" fill="#d9b51a"/></svg>
        <span>Rue des Tanneries 9<br>1700 Fribourg</span>
      </div>
    </div>
  </div>

  <footer class="front-band">Sports massage - Therapeutic massage - Relaxing massage</footer>
</section>

<section class="card card--back" aria-label="Verso">
  <div class="back-band">
    <div class="identity">
      <div class="identity__square"></div>
      <div>
        <div class="identity__name">Loïc Vermande</div>
        <div class="identity__role">Massothérapeute / Préparateur mental</div>
      </div>
    </div>
  </div>
</section>

</body>
</html>
```